Finance cashflow waterfall graphic

Recreate "Cashflow Waterfall Example 1" - waterfall term used to explain the different accounts and priority that need to be paid as part of a apartment building / project. Create simple, business professional graphic for real estate report. Check the inspiration image but change to dorm building, no people - potentially combine the two images... Ideally editable so I can change the names of the accounts / colors / etc.

```html
<!DOCTYPE html>
<html lang="en">
<head>
<meta charset="utf-8">
<title>Cashflow Waterfall</title>
<link href="https://fonts.googleapis.com/css2?family=Anton&display=swap" rel="stylesheet">
<style>
  :root {
    --bg: #ffffff;
    --band-top: #9fc3f9;
    --band-bottom: #ffffff;
    --tank-start: #0f86b7;
    --tank-end: #2f8ee8;
    --ink: #0b2440;
    --label-white: #ffffff;
    --drop: #2566c9;
    --tap: #0d0d0d;
    --ribbon-dark-top: #2a85d6;
    --ribbon-dark-mid: #0c2c69;
    --ribbon-dark-bottom: #020c22;
    --chevron: #2468cc;
  }
  * { margin: 0; padding: 0; box-sizing: border-box; }
  html, body { width: 745px; height: 1200px; overflow: hidden; background: var(--bg); }
  .canvas {
    position: relative;
    width: 745px;
    height: 1200px;
    overflow: hidden;
    background: var(--bg);
    font-family: "Anton", "Arial Narrow", sans-serif;
    color: var(--ink);
  }
  .flow-band { position: absolute; inset: 0; width: 745px; height: 1200px; }
  .bank-ribbon {
    position: absolute; left: 52px; top: 49px; width: 150px; height: 290px;
    filter: drop-shadow(-10px 10px 12px rgba(0,0,0,.28));
  }
  .bank-title {
    position: absolute; left: 52px; top: 134px; width: 150px;
    text-align: center; font-size: 66px; line-height: 1; color: var(--label-white);
    letter-spacing: -1px;
  }
  .revenue-title {
    position: absolute; left: 50px; top: 348px; width: 154px;
    font-size: 55px; line-height: 1; letter-spacing: -0.5px; text-align: center;
  }
  .drop { position: absolute; width: 7px; height: 11px; }
  .tank {
    position: absolute;
    filter: drop-shadow(-14px 10px 12px rgba(0,0,0,.32));
  }
  .tank svg { display: block; width: 100%; height: 100%; }
  .tap { position: absolute; width: 33px; height: 18px; }
  .account-label {
    position: absolute; font-size: 13px; line-height: 1.0; white-space: nowrap;
  }
  .split-label { font-size: 10px; line-height: 1.1; letter-spacing: -0.2px; }
  .split-label.right { text-align: right; }
  .split-value {
    position: absolute; inset: 0; display: flex; align-items: center; justify-content: center;
    color: var(--label-white); font-size: 17px; padding-top: 2px;
  }
</style>
</head>
<body>
<div class="canvas">

  <svg width="0" height="0" style="position:absolute" aria-hidden="true">
    <defs>
      <linearGradient id="tankFill" x1="0" y1="1" x2="1" y2="0">
        <stop offset="0" stop-color="var(--tank-start)"/>
        <stop offset="1" stop-color="var(--tank-end)"/>
      </linearGradient>
      <linearGradient id="bandFill" x1="0" y1="0" x2="0" y2="1">
        <stop offset="0" stop-color="var(--band-top)"/>
        <stop offset="1" stop-color="var(--band-bottom)"/>
      </linearGradient>
      <linearGradient id="ribbonDark" x1="0" y1="0" x2="0" y2="1">
        <stop offset="0" stop-color="var(--ribbon-dark-top)"/>
        <stop offset=".5" stop-color="var(--ribbon-dark-mid)"/>
        <stop offset="1" stop-color="var(--ribbon-dark-bottom)"/>
      </linearGradient>
      <symbol id="tankShape" viewBox="0 0 100 100" preserveAspectRatio="none">
        <path d="M0,3 C28,0 60,-1 100,1.5 V86 Q100,100 84,100 H14 Q0,100 0,88 Z" fill="url(#tankFill)"/>
      </symbol>
      <symbol id="tapShape" viewBox="0 0 33 18">
        <rect x="9" y="0" width="10" height="2.6" rx="1" fill="var(--tap)"/>
        <rect x="12.6" y="1.5" width="3" height="4" fill="var(--tap)"/>
        <path d="M0,5 H24 Q32,5 32,13 V17 H28 V13 Q28,9 24,9 H0 Z" fill="var(--tap)"/>
      </symbol>
      <symbol id="dropShape" viewBox="0 0 7 11">
        <path d="M3.5,0 C4.5,3 7,5.5 7,7.5 A3.5,3.5 0 0 1 0,7.5 C0,5.5 2.5,3 3.5,0 Z" fill="var(--drop)"/>
      </symbol>
    </defs>
  </svg>

  <svg class="flow-band" viewBox="0 0 745 1200" aria-hidden="true">
    <path d="M0,0 H540 C370,55 275,190 275,340 C275,620 430,900 625,1118 C330,840 40,520 0,185 Z" fill="url(#bandFill)"/>
  </svg>

  <svg class="bank-ribbon" viewBox="0 0 150 290" aria-hidden="true">
    <path d="M0,16 Q0,0 20,0 H130 Q150,0 150,16 V248 C120,245 40,246 0,250 Z" fill="url(#tankFill)"/>
    <path d="M16,250 L74,289 L134,250 Z" fill="var(--chevron)"/>
    <path d="M16,10 H134 V255 C110,268 90,274 74,276 C58,274 38,268 16,255 Z" fill="url(#ribbonDark)"/>
  </svg>
  <div class="bank-title">BANK</div>
  <svg class="drop" style="left:120px;top:339px" aria-hidden="true"><use href="#dropShape"/></svg>

  <div class="revenue-title">REVENUE</div>

  <!-- Revenue -->
  <div class="tank" style="left:50px;top:408px;width:149px;height:130px"><svg aria-hidden="true"><use href="#tankShape"/></svg></div>
  <svg class="tap" style="left:199px;top:514px" aria-hidden="true"><use href="#tapShape"/></svg>
  <svg class="drop" style="left:226px;top:536px" aria-hidden="true"><use href="#dropShape"/></svg>

  <!-- Operating Expenses -->
  <div class="account-label" style="left:194px;top:548px">Operating Expenses</div>
  <div class="tank" style="left:192px;top:576px;width:109px;height:95px"><svg aria-hidden="true"><use href="#tankShape"/></svg></div>
  <svg class="tap" style="left:300px;top:648px" aria-hidden="true"><use href="#tapShape"/></svg>
  <svg class="drop" style="left:327px;top:670px" aria-hidden="true"><use href="#dropShape"/></svg>

  <!-- Debt Payment -->
  <div class="account-label" style="left:298px;top:688px">Debt Payment</div>
  <div class="tank" style="left:296px;top:710px;width:87px;height:78px"><svg aria-hidden="true"><use href="#tankShape"/></svg></div>
  <svg class="tap" style="left:382px;top:766px" aria-hidden="true"><use href="#tapShape"/></svg>
  <svg class="drop" style="left:409px;top:788px" aria-hidden="true"><use href="#dropShape"/></svg>

  <!-- Assets Management Fees -->
  <div class="account-label" style="left:379px;top:799px">Assets<br>Management Fees</div>
  <div class="tank" style="left:378px;top:833px;width:71px;height:67px"><svg aria-hidden="true"><use href="#tankShape"/></svg></div>
  <svg class="tap" style="left:449px;top:878px" aria-hidden="true"><use href="#tapShape"/></svg>
  <svg class="drop" style="left:476px;top:900px" aria-hidden="true"><use href="#dropShape"/></svg>

  <!-- Recapitalization Accounts -->
  <div class="account-label" style="left:445px;top:912px">Recapitalization<br>Accounts</div>
  <div class="tank" style="left:444px;top:945px;width:56px;height:57px"><svg aria-hidden="true"><use href="#tankShape"/></svg></div>
  <svg class="tap" style="left:500px;top:980px" aria-hidden="true"><use href="#tapShape"/></svg>
  <svg class="drop" style="left:527px;top:1002px" aria-hidden="true"><use href="#dropShape"/></svg>

  <!-- Incentive fees -->
  <div class="account-label" style="left:499px;top:1015px">Incentive<br>fees</div>
  <div class="tank" style="left:498px;top:1048px;width:43px;height:48px"><svg aria-hidden="true"><use href="#tankShape"/></svg></div>
  <svg class="tap" style="left:540px;top:1067px" aria-hidden="true"><use href="#tapShape"/></svg>
  <svg class="drop" style="left:567px;top:1089px" aria-hidden="true"><use href="#dropShape"/></svg>

  <!-- Distribution split -->
  <div class="account-label split-label right" style="left:470px;top:1110px;width:130px">Sustainment Reserves/<br>Member Distribution</div>
  <div class="account-label split-label" style="left:613px;top:1110px">Private Returns/<br>Managing Member distribution</div>
  <div class="tank" style="left:532px;top:1140px;width:68px;height:33px">
    <svg aria-hidden="true"><use href="#tankShape"/></svg>
    <div class="split-value">60%</div>
  </div>
  <div class="tank" style="left:613px;top:1140px;width:40px;height:33px">
    <svg aria-hidden="true"><use href="#tankShape"/></svg>
    <div class="split-value">40%</div>
  </div>

</div>
</body>
</html>
```